Feature film needs look book digital brochure - Media/Investor's package

Looking for a designer to create an edgy, eye popping visual representation of my film to get interest from investors, producers and actors, along with Investor and Sponsorship information. Basically it would introduce the project and in about 9-13 pages; give an overview of the film, why to invest, an artistic statement and potential casting ideas and an introduction to the key crew. I have included images (probably more than you need), our film's key art (harbor glass final image & bib logo), and our company (Corvane)'s logo. I've also included samples for another film (tqwl_proposal.pdf) and a proposal I already did for the film. The sample for the other film is more visual and something I'd like to emulate.

The film is called Harbor Glass: a sports drama about two triathletes who overcome their personal demons to train for and compete in the biggest race of their lives.

```html
<!DOCTYPE html>
<html lang="en">
<head>
<meta charset="utf-8">
<title>Harbor Glass Proposal – Background and Need</title>
<link href="https://fonts.googleapis.com/css2?family=Tinos:ital,wght@0,400;0,700;1,400;1,700&display=swap" rel="stylesheet">
<style>
  :root {
    --sky-top: #b9cfdf;
    --sky-haze: #e6ecee;
    --horizon: #d9c48a;
    --road-glow: #b08a45;
    --ground: #5b4a33;
    --ground-deep: #2a241e;
    --heading-grey: #7b7a72;
    --ink: #111111;
    --paper-white: #ffffff;
    --accent-gold: #d8a62a;
  }
  * { margin: 0; padding: 0; box-sizing: border-box; }
  html, body { width: 885px; height: 1200px; overflow: hidden; }
  body { font-family: "Tinos", "Times New Roman", serif; }

  .page {
    position: relative;
    width: 885px;
    height: 1200px;
    overflow: hidden;
  }
  .page-backdrop {
    position: absolute;
    inset: 0;
    background:
      radial-gradient(ellipse 120px 380px at 442px 520px, rgba(255,225,150,0.55), rgba(255,225,150,0) 100%),
      linear-gradient(to bottom,
        var(--sky-top) 0%,
        var(--sky-haze) 14%,
        #f1efe6 30%,
        var(--horizon) 37%,
        var(--road-glow) 44%,
        var(--ground) 58%,
        #3e342a 78%,
        var(--ground-deep) 100%);
  }

  .section-title {
    position: absolute;
    font-weight: 700;
    text-transform: uppercase;
    letter-spacing: 2px;
    line-height: 1;
  }
  .section-title--need {
    left: 142px;
    top: 96px;
    font-size: 38px;
    color: var(--heading-grey);
  }
  .section-title--approach {
    left: 82px;
    top: 630px;
    font-size: 31px;
    color: var(--paper-white);
  }

  .section-body {
    position: absolute;
    font-size: 15px;
    line-height: 17.8px;
  }
  .section-body p + p { margin-top: 17.8px; }
  .section-body--need {
    left: 143px;
    top: 154px;
    width: 590px;
    color: var(--ink);
  }
  .section-body--approach {
    left: 85px;
    top: 695px;
    width: 762px;
    color: var(--paper-white);
  }

  .page-footer {
    position: absolute;
    left: 450px;
    right: 0;
    top: 1136px;
  }
  .footer-title {
    display: block;
    text-align: right;
    padding-right: 36px;
    font-style: italic;
    font-size: 14px;
    color: var(--accent-gold);
  }
  .footer-rule {
    height: 2px;
    background: var(--paper-white);
    margin-top: 3px;
  }
  .footer-credit {
    display: block;
    text-align: right;
    padding-right: 36px;
    margin-top: 3px;
    font-style: italic;
    font-weight: 700;
    font-size: 11px;
    color: var(--paper-white);
  }
</style>
</head>
<body>
<main class="page">
  <div class="page-backdrop" role="img" aria-label="Photograph of an empty country road stretching to the horizon at sunset under a pale sky"></div>

  <h1 class="section-title section-title--need">Background and Need</h1>
  <div class="section-body section-body--need">
    <p>The idea for Harbor Glass started when Daniel and Marisol, the writers/producers, went to volunteer at Summit Coast Triathlon in 2010.</p>
    <p>The subject matter is loosely drawn from both of our own personal landscapes. As a participant in triathlons and marathons Daniel has gone through many of the moments that Trevor and Cora, our main characters, go through in their training journey. Of course, true stories come from the heart and many of the emotional moments in Harbor Glass are expressions of questions and feelings both of us have gone through in our lives. With our movie, we have a story of two characters: the first is a man with a single-minded focus, who only cares about redeeming himself, not for fame or glory, but for his own fulfillment. The second, a woman who turns to an endurance race to pick up the pieces of what she views as a postponed life of living for the pleasure of others.</p>
    <p>Harbor Glass is a story that unfolds in the emotions we keep from each other and how understanding each other can lead to a greater understanding of ourselves. As a newly married couple, Marisol and Daniel both realize that relationships with people take work, because we are ever-evolving creatures and each of our experiences creates the new version of us.<br>
    This is why we are well positioned to make this movie. Daniel has worked in the film industry for several years, and combined with Marisol’s background in marketing and business management, this new adventure into an independent filmmaking career draws a large parallel with the theme of the film. In making this movie, we are entering the undiscovered country, the future, much like their characters face their own uncertainty throughout the movie.</p>
  </div>

  <h2 class="section-title section-title--approach">Approach, Structure and Style</h2>
  <div class="section-body section-body--approach">
    <p>Harbor Glass will be an aesthetically bold and sonically rich movie set to a patient pace with action elements and drama surrounding the “chase” of a big race. We will feel the interplay of possibility and realized potential, grounded in human emotion and set against the wonderful backdrop of endurance sports.</p>
    <p>The greatest moments in film happen when a viewer can’t explain what was so beautiful or emotional in a scene, and yet they are moved regardless. It is the energy of a moment that touches people like music. In attempting to express something cinematic, we want to explore, through this film, the intimate details of human feelings and have the audience see those things. But too much of an explanation before this film is made might take away from that. We want to find the cinematic moments that make this movie necessary by itself. The look of the film will be very painterly, inspiring, visceral, sexy, with a vibrant color palette. We aim to capture the glitzy, global nature of triathlon and simulate conditions in a variety of countries, using archival footage and using live race footage from real races to add realism to our race scenes. There are dozens of races in British Columbia, the planned hub of our filmmaking, to grab footage and we have relationships with race directors that will facilitate this, with plans to partner with races and triathlon product companies to make the movie authentic.</p>
    <p>With this approach, a mix of traditional and loose filmmaking, we are sprouting seeds and seeing where they grow. The film has a large number of exterior scenes, many of which are not weather dependent, and will be filmed around Vancouver, British Columbia. With plans to commence principle photography this fall 2014, the filming can begin</p>
  </div>

  <footer class="page-footer">
    <span class="footer-title">Harbor Glass Proposal</span>
    <div class="footer-rule"></div>
    <span class="footer-credit">Fenwick Film Grant – June 12, 2014</span>
  </footer>
</main>
</body>
</html>
```